Commercial cleaning business needs a trifold brochure to spotlight janitorial services offered.

Looking for a catchy, creative, trifold brochure to give a description of services offered. This would be used for new potential customers. Our primary colors are royal blue, light gray, and white as included in our logo. The logo does include "restoration", however we only want this brochure to be focused solely on the commercial cleaning side for janitorial services as we already purchased a brochure for the restoration. You can visit our website to get a better idea. www.vtlqservices.example

```html
<!DOCTYPE html>
<html lang="en">
<head>
<meta charset="utf-8">
<title>VTLQ Commercial Cleaning Trifold</title>
<link rel="stylesheet" href="https://fonts.googleapis.com/css2?family=Oswald:wght@400;500;600;700&family=Open+Sans:wght@400;600;700;800&display=swap">
<style>
:root{
  --royal:#2a2a7a;
  --royal-deep:#23236b;
  --gray:#a7a7aa;
  --gray-light:#e9e9eb;
  --white:#ffffff;
  --ink:#1c1c2a;
  --lilac:#9c98c8;
  --stage:#474747;
}
*{margin:0;padding:0;box-sizing:border-box}
html,body{width:877px;height:1200px;overflow:hidden}
body{background:var(--stage);font-family:"Open Sans",sans-serif;color:var(--ink);position:relative}
.sheet{position:absolute;left:96px;width:684px;height:483px;overflow:hidden;background:var(--white);box-shadow:0 4px 14px rgba(0,0,0,.45)}
.sheet--outside{top:82px}
.sheet--inside{top:641px}
.sheet__art{position:absolute;inset:0}
.panel{position:absolute;top:0;width:228px;height:483px}
.panel--1{left:0}.panel--2{left:228px}.panel--3{left:456px}
.fold{position:absolute;top:0;width:1px;height:483px;background:rgba(0,0,0,.07)}
.abs{position:absolute}
.heading{font-family:"Oswald",sans-serif;font-weight:400;font-size:20px;line-height:1;color:var(--ink);letter-spacing:-.2px;white-space:nowrap}
.heading b{font-weight:600;color:var(--royal)}
.heading--rule{border-bottom:1.2px solid var(--royal);padding-bottom:4px}
.heading--stack{font-size:18.5px;line-height:23px;letter-spacing:-.3px}
.body{font-size:6.9px;line-height:9.9px;text-align:justify;color:var(--ink)}
.body p+p{margin-top:9px}
.photo{position:absolute;background:linear-gradient(150deg,#dfe3ea,#a9b2c2 60%,#6f7a92)}
.photo--round{border-radius:50%;border:4px solid var(--royal)}
.lead{font-size:9.6px;line-height:13.2px;text-align:center}
.lead b{color:var(--royal);font-weight:700}
.motto{border:1.4px solid var(--royal);text-align:center;font-family:"Oswald",sans-serif;font-weight:700;color:var(--royal);font-size:19px;line-height:21px;padding:4px 0 3px;background:var(--white)}
.pill{border:1.4px solid var(--royal);border-radius:12px;text-align:center;font-family:"Oswald",sans-serif;font-weight:500;color:var(--royal);font-size:14px;line-height:19px}
.contact{font-size:9.4px;line-height:14px;text-align:center;color:var(--ink)}
.contact svg{vertical-align:-1px;margin-right:3px}
.phone-pill{background:var(--royal);border-radius:13px;color:var(--white);font-family:"Oswald",sans-serif;font-weight:700;font-size:18px;line-height:26px;text-align:center}
.phone-pill svg{vertical-align:-3px;margin-right:4px}
.social{width:15px;height:15px;border-radius:50%;background:var(--royal)}
.url{font-size:10.5px;letter-spacing:1.3px;color:var(--white);text-align:center}
.url b{font-weight:700}
.tagline{color:var(--white);font-size:12px;line-height:17px}
.tagline b{font-weight:800}
.brand{text-align:center}
.brand__row{display:flex;align-items:center;justify-content:center;gap:7px}
.brand__dot{width:22px;height:22px;border-radius:50%;background:var(--royal)}
.brand__name{font-family:"Open Sans",sans-serif;font-weight:800;font-size:30px;color:var(--royal);letter-spacing:1px;line-height:1}
.brand__sub{font-size:8.4px;font-weight:600;color:var(--royal);margin-top:8px}
.hero-title{font-family:"Oswald",sans-serif;font-weight:700;color:var(--white);font-size:33px;line-height:33px;text-align:center;letter-spacing:.5px}
.callnow{font-family:"Oswald",sans-serif;font-weight:600;color:var(--white);font-size:19px;text-align:center;display:flex;align-items:center;gap:8px;justify-content:center}
.callnow::before,.callnow::after{content:"";width:40px;height:1px;background:var(--white)}
.big-phone{font-family:"Oswald",sans-serif;font-weight:700;color:var(--white);font-size:29px;text-align:center;letter-spacing:.3px;line-height:1}
.panel--dots{background:linear-gradient(180deg,#f1f1f3,#fafafa 60%)}
.panel--blue{background:var(--royal)}
.heading--light{color:var(--white)}
.heading--light b{color:var(--white)}
.intro{color:var(--white);font-size:9.6px;line-height:13.4px}
.services{list-style:none;color:var(--white);font-size:9.6px;line-height:13.4px}
.services li{display:flex;gap:6px;margin-bottom:3.3px}
.services svg{flex:none;margin-top:2px}
.services b{font-weight:700}
.services span{font-weight:400}
.supplies{background:var(--white);text-align:center;font-family:"Oswald",sans-serif;font-weight:400;color:var(--royal);font-size:17px;line-height:24px}
.supplies b{font-weight:600}
.deco-circle{position:absolute;border-radius:50%;background:var(--lilac);opacity:.85}
.value{position:absolute;left:28px;width:180px;height:46px;display:flex;align-items:center}
.value__icon{width:43px;height:43px;border-radius:50%;border:1.2px solid var(--royal);display:flex;align-items:center;justify-content:center;background:var(--white);flex:none}
.value__text{margin-left:13px;border-left:1px solid #c9c9d6;padding-left:8px}
.value__name{font-weight:700;color:var(--royal);font-size:11.5px;line-height:14px}
.value__desc{font-size:6.6px;line-height:9.4px;color:var(--ink)}
</style>
</head>
<body>

<!-- Outside of the trifold -->
<section class="sheet sheet--outside">
  <svg class="sheet__art" width="684" height="483" viewBox="0 0 684 483" aria-hidden="true">
    <defs>
      <linearGradient id="top-fade" x1="0" y1="0" x2="0" y2="1">
        <stop offset="0" stop-color="#efeff1"/><stop offset="1" stop-color="#ffffff"/>
      </linearGradient>
      <linearGradient id="cover-fade" x1="0" y1="0" x2="1" y2="0">
        <stop offset="0" stop-color="#d9d9dc"/><stop offset="1" stop-color="#f4f4f5"/>
      </linearGradient>
    </defs>
    <rect width="684" height="483" fill="url(#top-fade)"/>
    <rect x="456" width="228" height="483" fill="url(#cover-fade)"/>
    <path d="M0,268 C80,320 170,372 300,398 C430,420 570,408 684,362 L684,378 C570,424 430,432 300,412 C170,388 70,338 0,296 Z" fill="var(--gray)"/>
    <path d="M0,300 C80,340 160,385 260,402 C380,424 540,420 684,382 L684,483 L0,483 Z" fill="var(--royal)"/>
    <path d="M456,180 C520,140 600,118 684,100 L684,120 C600,128 520,150 456,190 Z" fill="var(--royal)"/>
    <path d="M456,192 C520,154 600,132 684,122 L684,134 C600,140 520,162 456,200 Z" fill="var(--gray)"/>
  </svg>

  <div class="panel panel--1">
    <h2 class="heading heading--rule abs" style="left:27px;top:25px;width:177px">OUR <b>MISSION</b></h2>
    <div class="body abs" style="left:27px;top:60px;width:178px">
      <p>Valley Tri-Lake Quality Maintenance is committed to providing an unsurpassed level of janitorial services and building long-lasting relationships with clients. We accomplish this by using modern technology to communicate effectively with client's and employees.</p>
      <p>Our team leaders assist clients in defining their needs and communicate those needs to our employees. We act with integrity in all aspects of our business at all times. Our goal is to deliver a consistently high level of janitorial services that are within your budget.</p>
      <p>We hold each and every client in the highest regard and promise to provide exceptional service. This is accomplished by experienced, professional employees who follow our company's meticulous cleaning standards. We provide quality cleaning services, exceptional customer service, scheduled site inspections, and customer surveys while keeping communication lines open for our customers so that their every need is fulfilled.</p>
    </div>
    <div class="photo photo--round" role="img" aria-label="Photo of two smiling cleaners in uniforms holding a mop and gloves" style="left:57px;top:280px;width:150px;height:150px"></div>
    <p class="tagline abs" style="left:27px;top:437px">It's not about the <b>Cleaning,</b><br>it's about the <b>Communication.</b></p>
  </div>

  <div class="panel panel--2">
    <p class="lead abs" style="left:20px;top:28px;width:188px">We <b>INSPECT</b> our work,<br><b>COMMUNICATE</b> with our clients, and<br><b>ADJUST</b> where needed in order to<br>provide the best in class service for<br>your facilities, clients, and staff.</p>
    <div class="photo" role="img" aria-label="Photo of a basket of cleaning supplies with rubber gloves" style="left:58px;top:100px;width:112px;height:95px;border-radius:8px;background:radial-gradient(circle at 50% 55%,#f0a8c0,#9fd3e6 45%,#ffffff 75%)"></div>
    <div class="motto abs" style="left:23px;top:200px;width:182px">Dedication Through<br>Communication</div>
    <div class="pill abs" style="left:44px;top:262px;width:141px">Contact Info</div>
    <p class="contact abs" style="left:10px;top:292px;width:208px">
      <svg width="6" height="8" viewBox="0 0 6 8"><path d="M3 0a3 3 0 0 0-3 3c0 2.2 3 5 3 5s3-2.8 3-5a3 3 0 0 0-3-3zm0 4.2A1.2 1.2 0 1 1 3 1.8a1.2 1.2 0 0 1 0 2.4z" fill="var(--royal)"/></svg>14 North Alder Street<br>Mt. Harlow, Kentucky 40399
    </p>
    <p class="contact abs" style="left:10px;top:326px;width:208px">
      <svg width="10" height="7" viewBox="0 0 10 7"><rect x=".5" y=".5" width="9" height="6" fill="none" stroke="var(--royal)"/><path d="M.5.5 5 4 9.5.5" fill="none" stroke="var(--royal)"/></svg>dmorrow@vtlqservices.example
    </p>
    <div class="phone-pill abs" style="left:20px;top:348px;width:187px">
      <svg width="16" height="16" viewBox="0 0 16 16"><path d="M4 1.5 6 4.5 4.6 6.2c.8 1.9 2.3 3.4 4.2 4.3l1.6-1.4 3 2-1.5 2.6C6.8 13.6 2.4 9.2 1.3 3.1z" fill="none" stroke="var(--white)" stroke-width="1.2" stroke-linejoin="round"/></svg>|&nbsp;1-866-555-0148
    </div>
    <div class="social abs" style="left:106px;top:386px"></div>
    <svg class="abs" style="left:105px;top:432px" width="16" height="14" viewBox="0 0 16 14" aria-hidden="true"><path d="M3 12 13 2M9 2h4v4" fill="none" stroke="var(--white)" stroke-width="1.2"/></svg>
    <p class="url abs" style="left:0;top:452px;width:228px"><b>www.vtlqservices</b>.example</p>
  </div>

  <div class="panel panel--3">
    <div class="brand abs" style="left:0;top:52px;width:228px">
      <div class="brand__row"><span class="brand__dot"></span><span class="brand__name">VTLQ</span></div>
      <p class="brand__sub">Commercial Cleaning &amp; Restoration</p>
    </div>
    <div class="photo" role="img" aria-label="Photo of cleaners vacuuming and wiping desks in a bright office" style="left:0;top:140px;width:228px;height:175px;clip-path:polygon(0 30%,40% 12%,100% 0,100% 100%,0 100%);background:linear-gradient(160deg,#eef0f3,#c7ccd6 50%,#5e6378)"></div>
    <svg class="abs" style="left:0;top:290px" width="228" height="120" viewBox="0 0 228 120" aria-hidden="true">
      <path d="M0,30 C60,-5 170,-5 228,25 L228,70 C170,105 60,112 0,90 Z" fill="var(--royal)"/>
      <path d="M0,94 C70,116 170,104 228,72 L228,80 C170,112 70,124 0,102 Z" fill="var(--gray-light)"/>
    </svg>
    <h1 class="hero-title abs" style="left:0;top:303px;width:228px">COMMERCIAL<br>CLEANING</h1>
    <svg class="abs" style="left:168px;top:390px" width="46" height="32" viewBox="0 0 46 32" aria-hidden="true">
      <path d="M4 3 9 9 7 12c1.5 4 4.5 7 8.5 9l3-2 6 4-2.5 5C11 27 3 18 1 5z" fill="none" stroke="var(--white)" stroke-width="1.4" stroke-linejoin="round"/>
      <text x="19" y="16" font-family="Oswald,sans-serif" font-weight="600" font-size="8" fill="var(--white)">24/7</text>
    </svg>
    <p class="callnow abs" style="left:0;top:422px;width:228px">CALL NOW</p>
    <p class="big-phone abs" style="left:0;top:448px;width:228px">1-866-555-0148</p>
  </div>
  <span class="fold" style="left:228px"></span><span class="fold" style="left:456px"></span>
</section>

<!-- Inside of the trifold -->
<section class="sheet sheet--inside">
  <div class="panel panel--1 panel--dots">
    <h2 class="heading heading--rule heading--stack abs" style="left:27px;top:22px;width:177px">EXPERIENCE<br><b>HIGH-TECH EFFICIENCY</b></h2>
    <div class="body abs" style="left:27px;top:88px;width:175px">
      <p>Valley Tri-Lake Quality Maintenance follows a technology-based service delivery process. In our company, employees communicate with each other using smartphone/tablet apps so that they can track every cleaning team's whereabouts.</p>
      <p>This enables main office managers to efficiently monitor work progress in real time. With this high-tech infrastructure in place, our cleaners can be able to relay on-the-spot customer requests to us immediately. We can then issue instructions just as quickly to employees on site.</p>
    </div>
    <span class="deco-circle" style="left:85px;top:218px;width:26px;height:26px"></span>
    <span class="deco-circle" style="left:115px;top:221px;width:50px;height:50px"></span>
    <div class="photo" role="img" aria-label="Photo of two cleaners wiping desks in a modern white office" style="left:0;top:238px;width:228px;height:245px;clip-path:ellipse(100% 100% at 0% 100%);background:linear-gradient(170deg,#f4f5f7,#d4d8df 45%,#8c93a3)"></div>
  </div>

  <div class="panel panel--2 panel--blue">
    <h2 class="heading heading--rule heading--light abs" style="left:23px;top:24px;width:176px;border-color:var(--white)"><b style="font-weight:400">SERVICES</b> <b>WE OFFER</b></h2>
    <p class="intro abs" style="left:23px;top:58px;width:190px">Our company specializes in cleaning medical facilities and class-A office spaces. You can contact us to request:</p>
    <ul class="services abs" style="left:23px;top:104px;width:195px">
      <li><svg width="10" height="10" viewBox="0 0 10 10"><circle cx="5" cy="5" r="4.4" fill="none" stroke="var(--white)" stroke-width=".9"/><path d="M3 5.1 4.4 6.4 7 3.7" fill="none" stroke="var(--white)" stroke-width=".9"/></svg><b>CARPET CLEANING</b></li>
      <li><svg width="10" height="10" viewBox="0 0 10 10"><circle cx="5" cy="5" r="4.4" fill="none" stroke="var(--white)" stroke-width=".9"/><path d="M3 5.1 4.4 6.4 7 3.7" fill="none" stroke="var(--white)" stroke-width=".9"/></svg><div><b>FLOOR CARE</b> <span>(Personalized Programs, Including Stripping and Waxing)</span></div></li>
      <li><svg width="10" height="10" viewBox="0 0 10 10"><circle cx="5" cy="5" r="4.4" fill="none" stroke="var(--white)" stroke-width=".9"/><path d="M3 5.1 4.4 6.4 7 3.7" fill="none" stroke="var(--white)" stroke-width=".9"/></svg><b>JANITORIAL SERVICES</b></li>
      <li><svg width="10" height="10" viewBox="0 0 10 10"><circle cx="5" cy="5" r="4.4" fill="none" stroke="var(--white)" stroke-width=".9"/><path d="M3 5.1 4.4 6.4 7 3.7" fill="none" stroke="var(--white)" stroke-width=".9"/></svg><b>WINDOW CLEANING</b></li>
      <li><svg width="10" height="10" viewBox="0 0 10 10"><circle cx="5" cy="5" r="4.4" fill="none" stroke="var(--white)" stroke-width=".9"/><path d="M3 5.1 4.4 6.4 7 3.7" fill="none" stroke="var(--white)" stroke-width=".9"/></svg><b>24- HOUR EMERGENCY WATER EXTRACTION SERVICES</b></li>
    </ul>
    <span class="deco-circle" style="left:147px;top:229px;width:50px;height:50px;background:#b7b4dc"></span>
    <span class="deco-circle" style="left:118px;top:251px;width:22px;height:22px;background:#b7b4dc"></span>
    <div class="photo photo--round" role="img" aria-label="Photo of three smiling cleaners in light blue uniforms beside a cleaning cart" style="left:-48px;top:215px;width:160px;height:160px;border-color:var(--white);background:linear-gradient(160deg,#e7eaf0,#8fc6e6 50%,#3c5a8a)"></div>
    <div class="photo photo--round" role="img" aria-label="Photo of hands holding a blue bucket full of cleaning supplies" style="left:80px;top:255px;width:135px;height:135px;border-color:var(--white);border-width:1.5px;background:radial-gradient(circle at 50% 60%,#3aa0e0,#e8a24a 45%,#2b2b3a 80%)"></div>
    <div class="supplies abs" style="left:25px;top:409px;width:177px">CALL US FOR <b>SUPPLIES</b></div>
    <p class="big-phone abs" style="left:0;top:441px;width:228px;font-size:30px">1-866-555-0148</p>
  </div>

  <div class="panel panel--3">
    <h2 class="heading heading--rule abs" style="left:27px;top:24px;width:175px">OUR <b>VISION</b></h2>
    <div class="body abs" style="left:27px;top:64px;width:172px">
      <p>Valley Tri-Lake Quality Maintenance will be one of the top independently owned commercial cleaning services, serving the central and eastern part of Kentucky.</p>
      <p>Our vision is to become the leader in commercial cleaning and building services industry by using modern technology to blaze the trail that others will follow when it comes to providing quality services and exceptional customer service.</p>
      <p>We will be relentless in our commitment to fulfill our vision and offer our clients personalized service.</p>
    </div>
    <h2 class="heading heading--rule abs" style="left:27px;top:221px;width:175px">OUR <b>CORE VALUES</b></h2>

    <div class="value" style="top:263px">
      <div class="value__icon"><svg width="22" height="22" viewBox="0 0 22 22"><path d="M4 11a7 7 0 0 1 12-5M18 11a7 7 0 0 1-12 5" fill="none" stroke="var(--royal)" stroke-width="1.6"/><path d="M16 2v4h-4M6 20v-4h4" fill="none" stroke="var(--royal)" stroke-width="1.6"/></svg></div>
      <div class="value__text"><p class="value__name">Consistency</p><p class="value__desc">If you say it, mean it. If you<br>mean it, do it.</p></div>
    </div>
    <div class="value" style="top:315px">
      <div class="value__icon"><svg width="22" height="22" viewBox="0 0 22 22"><path d="M11 12 7 8a2.2 2.2 0 0 1 4-2.4A2.2 2.2 0 0 1 15 8z" fill="none" stroke="var(--royal)" stroke-width="1.3"/><path d="M3 10v5l5 4M19 10v5l-5 4" fill="none" stroke="var(--royal)" stroke-width="1.3"/></svg></div>
      <div class="value__text"><p class="value__name">Kindness</p><p class="value__desc">Be the reason someone believes<br>in the goodness of people.</p></div>
    </div>
    <div class="value" style="top:367px">
      <div class="value__icon"><svg width="22" height="22" viewBox="0 0 22 22"><path d="M11 3v16M4 6h14M7 19h8" stroke="var(--royal)" stroke-width="1.3" fill="none"/><path d="M4 6 1.5 12h5zM18 6l-2.5 6h5z" fill="none" stroke="var(--royal)" stroke-width="1.1"/></svg></div>
      <div class="value__text"><p class="value__name">Balance</p><p class="value__desc">Give proper weight to every area<br>of one's life.</p></div>
    </div>
    <div class="value" style="top:419px">
      <div class="value__icon"><svg width="22" height="22" viewBox="0 0 22 22"><circle cx="11" cy="9" r="5" fill="none" stroke="var(--royal)" stroke-width="1.3"/><path d="M9 15h4v3H9z" fill="none" stroke="var(--royal)" stroke-width="1.2"/><path d="M11 6v3l2 1" stroke="var(--royal)" stroke-width="1.2" fill="none"/></svg></div>
      <div class="value__text"><p class="value__name">Motivation</p><p class="value__desc">Empower our team to be a part<br>of something bigger.</p></div>
    </div>
  </div>
  <span class="fold" style="left:456px"></span>
</section>

</body>
</html>
```